No logos or construction designs

Easy to read Carl Wexford Roofing, LLC (in red)

all other lettering in black I guess I am open to what the designers come up

Construction

Carl Wexford Roofing, LLC office 555-2918463 fax 555-813-904 3875 Tamarind Ave W Brenford Falls, Orland 40219
Carl@CarlWexfordRoofing.example Residential Commerical
Carl Wexford cell 555-362-1187

```html
<!DOCTYPE html>
<html lang="en">
<head>
<meta charset="utf-8">
<title>Carl Wexford Roofing, LLC – Business Card</title>
<link rel="stylesheet" href="https://fonts.googleapis.com/css2?family=Oswald:wght@300;700&family=PT+Sans+Narrow:wght@700&display=swap">
<style>
  :root {
    --brand-red: #d42027;
    --ink: #111111;
    --paper: #ffffff;
    --backdrop: #e9e7e4;
  }
  * { box-sizing: border-box; margin: 0; padding: 0; }
  html, body {
    width: 1200px; height: 1000px; overflow: hidden;
    background: var(--backdrop);
  }
  .business-card {
    position: absolute; left: 348px; top: 60px;
    width: 504px; height: 880px;
    background: var(--brand-red);
    padding: 32px;
  }
  .card-face {
    position: relative; width: 100%; height: 100%;
    background: var(--paper);
    overflow: hidden;
  }
  .company-name {
    position: absolute; left: 30px; top: 36px;
    font-family: "Oswald", sans-serif; font-weight: 700;
    font-size: 56px; line-height: 0.95; letter-spacing: 0;
    color: var(--brand-red); text-transform: uppercase;
    white-space: nowrap;
  }
  .company-name .suffix { font-size: 36px; }
  .title-bar {
    position: absolute; left: 18px; top: 170px;
    width: 390px; height: 18px; background: var(--ink);
  }
  .services {
    position: absolute; left: 30px; top: 236px; right: 24px;
    font-family: "Oswald", sans-serif; font-weight: 300;
    font-size: 23px; color: var(--brand-red); text-transform: uppercase;
    white-space: nowrap;
  }
  .contact-name {
    position: absolute; left: 58px; top: 270px;
    font-family: "PT Sans Narrow", sans-serif; font-weight: 700;
    font-size: 34px; color: var(--ink); text-transform: uppercase;
  }
  .divider {
    position: absolute; left: 30px; top: 330px;
    width: 380px; height: 2px; background: var(--brand-red);
  }
  .contact-labels, .contact-values {
    position: absolute; list-style: none;
    font-family: "PT Sans Narrow", sans-serif; font-weight: 700;
    font-size: 21px; line-height: 31px; color: var(--ink);
    white-space: nowrap;
  }
  .contact-labels { left: 30px; top: 346px; text-transform: uppercase; }
  .contact-values { right: 24px; top: 474px; text-align: right; }
  .footer-bar {
    position: absolute; left: 30px; bottom: 54px;
    width: 340px; height: 18px; background: var(--ink);
  }
</style>
</head>
<body>
  <article class="business-card">
    <div class="card-face">
      <h1 class="company-name">Carl Wexford<br>Roofing, <span class="suffix">LLC</span></h1>
      <div class="title-bar"></div>
      <p class="services">Residential and Commercial</p>
      <p class="contact-name">Carl Wexford</p>
      <div class="divider"></div>
      <ul class="contact-labels">
        <li>Telephone:</li>
        <li>Cell:</li>
        <li>Fax:</li>
        <li>Email:</li>
        <li>Address:</li>
      </ul>
      <ul class="contact-values">
        <li>555-2918463</li>
        <li>555-362-1187</li>
        <li>555-813-904</li>
        <li>Carl@CarlWexfordRoofing.example</li>
        <li>3875 Tamarind Ave W</li>
        <li>Brenford Falls, Orland 40219</li>
      </ul>
      <div class="footer-bar"></div>
    </div>
  </article>
</body>
</html>
```